Business Card for a Mortgage Agent (myself)

I need a business card for my new job as Mortgage Agent. The Broker's logo is to be on the card as well as the brokerage License number. Not sure if to include a photo or not. Info to be on card.
Dante Roux
Mortgage Agent
Lic # M47105386
Cell: 905-614-2753
Email: danterouxk.ma@fennmail.com
Web: www.karlvostermortgages.com
TPW Brokerage Lic. # 73918

```html
<!DOCTYPE html>
<html lang="en">
<head>
<meta charset="utf-8">
<title>Dante Roux – Mortgage Agent Business Card</title>
<link rel="stylesheet" href="https://fonts.googleapis.com/css2?family=Jost:wght@500&family=Arimo:wght@400&display=swap">
<style>
  :root {
    --navy: #0a4185;
    --gold: #fdc900;
    --white: #ffffff;
    --page: #e9eaec;
  }
  * { box-sizing: border-box; margin: 0; padding: 0; }
  html, body { width: 1200px; height: 900px; overflow: hidden; }
  body {
    background: var(--page);
    display: flex;
    flex-direction: column;
    align-items: center;
    justify-content: center;
    gap: 40px;
    font-family: "Arimo", Arial, sans-serif;
  }
  .card {
    position: relative;
    width: 700px;
    height: 400px;
    overflow: hidden;
    box-shadow: 0 6px 18px rgba(0, 0, 0, 0.18);
  }

  /* Back side */
  .card-back {
    background: var(--navy);
    display: flex;
    align-items: center;
    justify-content: center;
  }
  .brand {
    display: flex;
    align-items: center;
    gap: 18px;
    font-family: "Jost", "Futura", sans-serif;
    font-weight: 500;
    letter-spacing: 0.04em;
    text-transform: uppercase;
  }
  .brand-mark { background: var(--gold); flex: none; }
  .card-back .brand { color: var(--white); font-size: 38px; }
  .card-back .brand-mark { width: 46px; height: 46px; }

  /* Front side */
  .card-front { background: var(--white); }
  .wave { position: absolute; inset: 0; width: 100%; height: 100%; }
  .wave .band { fill: var(--navy); }
  .wave .swoosh { fill: var(--gold); }

  .card-front .brand {
    position: absolute;
    top: 54px;
    right: 44px;
    color: var(--navy);
    font-size: 19px;
    gap: 10px;
  }
  .card-front .brand-mark { width: 24px; height: 24px; }

  .agent { position: absolute; top: 56px; left: 56px; }
  .agent-name {
    font-family: "Jost", "Futura", sans-serif;
    font-weight: 500;
    font-size: 36px;
    line-height: 1;
    color: var(--gold);
    text-transform: uppercase;
  }
  .agent-title { font-size: 22px; color: var(--navy); margin-top: 4px; }

  .contact {
    position: absolute;
    top: 168px;
    left: 56px;
    list-style: none;
    color: var(--navy);
    font-size: 20px;
  }
  .contact li { display: flex; align-items: center; gap: 10px; height: 30px; }
  .contact svg { width: 20px; height: 20px; flex: none; }
  .contact .icon { fill: none; stroke: var(--gold); stroke-width: 2; stroke-linecap: round; stroke-linejoin: round; }
  .contact .domain { color: var(--gold); }

  .licence {
    position: absolute;
    right: 40px;
    bottom: 40px;
    text-align: right;
    font-size: 20px;
    line-height: 1.35;
    color: var(--gold);
  }
  .licence .number { color: var(--white); }
</style>
</head>
<body>

  <section class="card card-back" aria-label="Business card, back">
    <div class="brand"><span class="brand-mark"></span><span>Trellis Point Wealth</span></div>
  </section>

  <section class="card card-front" aria-label="Business card, front">
    <svg class="wave" viewBox="0 0 700 400" preserveAspectRatio="none" aria-hidden="true">
      <path class="swoosh" d="M0 320 C220 326 420 262 580 168 C440 266 250 334 0 342 Z"/>
      <path class="band" d="M0 350 C250 344 450 226 700 118 L700 400 L0 400 Z"/>
    </svg>

    <div class="brand"><span class="brand-mark"></span><span>Trellis Point Wealth</span></div>

    <header class="agent">
      <h1 class="agent-name">Dante Roux</h1>
      <p class="agent-title">Mortgage Agent</p>
    </header>

    <ul class="contact">
      <li>
        <svg viewBox="0 0 24 24"><path class="icon" d="M5 3h4l2 5-2.5 1.5a11 11 0 0 0 6 6L16 13l5 2v4a2 2 0 0 1-2 2A16 16 0 0 1 3 5a2 2 0 0 1 2-2z"/></svg>
        <span>905-614-2753</span>
      </li>
      <li>
        <svg viewBox="0 0 24 24"><rect class="icon" x="2" y="5" width="20" height="14" rx="1"/><path class="icon" d="M2 6l10 7 10-7"/></svg>
        <span>danterouxk.ma@fennmail.com</span>
      </li>
      <li>
        <svg viewBox="0 0 24 24"><circle class="icon" cx="12" cy="12" r="9"/><path class="icon" d="M3 12h18M12 3c3 3 3 15 0 18M12 3c-3 3-3 15 0 18"/></svg>
        <span>www.<span class="domain">karlvostermortgages</span>.com</span>
      </li>
    </ul>

    <p class="licence">
      Lic # <span class="number">M47105386</span><br>
      TPW Brokerage Lic. <span class="number"># 73918</span>
    </p>
  </section>

</body>
</html>
```